TIMBER DECK COMPANY FLYER

We need a flyer design for a Timber Decking company, we specialise in timber decks, stairs, privacy screens, maintenance and pergolas. I have attatched some pictures which you can incorporate if you think they need cropping go for it. We offer amazing decks at affordable prices by qualified tradespeople.
My logo is a dull green I would like this to be changed to a more lime bright green please. Also my logo is too big I would like this logo halved in size please. And the colours in the brochure maybe a blackbackground with lime green and other colours you think will work. We will also beat any reputable Decking companies quote by 10%. Our decks add style, class, longjevity and practicality to any home. The final design should be modern and cutting edge.

Target Market(s)

home owners

Industry/Entity Type

It Company

Logo Text

CEDARLINE PATIO WORKS

Requirements
Must have
• DECKS
STAIRS
PERGOLAS
PRIVACY SCREENS
DECK MAINTENANCE

CONTACT-GORDON-0427158302

MUST HAVE LIKE US ON FRIENDBOOK LOGO

www.cedarlinepatioworks.com.au
Nice to have
• Please let me know if need more photos etc

```html
<!DOCTYPE html>
<html lang="en">
<head>
<meta charset="utf-8">
<title>Cedarline Patio Works Flyer</title>
<link rel="stylesheet" href="https://fonts.googleapis.com/css2?family=Jost:ital,wght@0,300;0,400;0,500;0,700;1,400&display=swap">
<style>
  :root {
    --lime: #bcd631;
    --lime-deep: #a9c21f;
    --black: #0d0d0d;
    --white: #ffffff;
    --wood-dark: #4a2318;
    --wood-mid: #7a3a27;
    --wood-light: #9a5236;
    --backdrop: #e4e4e4;
    --social-blue: #3b5998;
  }
  * { box-sizing: border-box; margin: 0; padding: 0; }
  html, body { width: 1200px; height: 750px; overflow: hidden; }
  body {
    background: var(--backdrop);
    font-family: "Jost", "Futura", sans-serif;
    position: relative;
  }
  .flyer {
    position: absolute;
    top: 180px;
    width: 560px;
    height: 390px;
    overflow: hidden;
  }
  .flyer--front { left: 26px; }
  .flyer--back { left: 614px; background: var(--lime); }

  /* Front */
  .deck-photo {
    position: absolute; inset: 0;
    background: linear-gradient(160deg, var(--wood-dark) 0%, var(--wood-mid) 45%, var(--wood-light) 75%, var(--wood-mid) 100%);
  }
  .brand {
    position: absolute; left: 48px; top: 30px;
    display: flex; align-items: flex-start; gap: 14px;
  }
  .brand__square { width: 38px; height: 38px; background: var(--white); }
  .brand__name {
    color: var(--white); font-weight: 300; font-size: 15px;
    line-height: 1.15; letter-spacing: 0.5px; width: 120px;
  }
  .call {
    position: absolute; left: 214px; top: 118px;
    font-size: 22px; line-height: 1.2; color: var(--white); white-space: nowrap;
  }
  .call__label { color: var(--lime); font-weight: 400; }
  .call__name { font-weight: 400; }
  .call__number { font-weight: 700; letter-spacing: 1px; }
  .services-disc {
    position: absolute; left: 226px; top: 152px;
    width: 300px; height: 300px; border-radius: 50%;
    background: var(--lime);
  }
  .services {
    position: absolute; left: 282px; top: 162px;
  }
  .services__title {
    color: var(--white); font-weight: 400; font-size: 23px; line-height: 1.2;
    letter-spacing: 0.5px; margin-bottom: 4px;
  }
  .services__list { list-style: none; }
  .services__item {
    color: var(--black); font-size: 18px; line-height: 1.3;
    display: flex; align-items: center; gap: 8px;
  }
  .services__item::before {
    content: ""; width: 7px; height: 7px; background: var(--black);
  }
  .web-strip {
    position: absolute; left: 0; right: 0; bottom: 0; height: 38px;
    background: var(--black);
    display: flex; align-items: center; padding-left: 22px;
    font-size: 17px; color: var(--white);
  }
  .web-strip__name { color: var(--lime); font-weight: 700; }

  /* Back */
  .tagline {
    position: absolute; left: 80px; top: 44px;
    font-style: italic; font-size: 19px; letter-spacing: 0.3px;
    color: var(--black); white-space: nowrap;
  }
  .tagline__alt { color: var(--white); }
  .photo-band {
    position: absolute; left: 0; right: 0; top: 76px; height: 150px;
    background: var(--lime-deep);
  }
  .photo {
    position: absolute; width: 124px; height: 96px;
    border: 2px solid var(--white);
  }
  .photo--garden { left: 24px; top: 8px; background: linear-gradient(135deg, #5e7a3e, #8a6a48); }
  .photo--pool { left: 150px; top: 24px; background: linear-gradient(135deg, #b86a45, #3aa1c9); }
  .photo--boards { left: 276px; top: 40px; background: linear-gradient(135deg, #a0583a, #c77d55); }
  .photo--spa { left: 402px; top: 50px; background: linear-gradient(135deg, #2f4a45, #6f8b83); }
  .social {
    position: absolute; left: 28px; top: 246px;
    display: flex; align-items: center; gap: 8px;
  }
  .social__square { width: 28px; height: 28px; background: var(--social-blue); }
  .social__text { color: var(--social-blue); font-size: 16px; font-weight: 500; }
</style>
</head>
<body>
  <section class="flyer flyer--front">
    <div class="deck-photo" role="img" aria-label="Photo of a finished reddish timber deck with boards running diagonally"></div>
    <div class="brand">
      <span class="brand__square"></span>
      <span class="brand__name">CEDARLINE PATIO WORKS</span>
    </div>
    <p class="call"><span class="call__label">CALL</span> <span class="call__name">Gordon</span> <span class="call__number">0427158302</span></p>
    <div class="services-disc"></div>
    <div class="services">
      <h2 class="services__title">OUR SERVICES:</h2>
      <ul class="services__list">
        <li class="services__item">Decks</li>
        <li class="services__item">Stairs</li>
        <li class="services__item">Pergolas</li>
        <li class="services__item">Privacy Screens</li>
        <li class="services__item">Deck Maintenance</li>
      </ul>
    </div>
    <div class="web-strip">www.<span class="web-strip__name">cedarlinepatioworks</span>.com.au</div>
  </section>

  <section class="flyer flyer--back">
    <p class="tagline">“STYLISH, <span class="tagline__alt">CLASSY,</span> LONGJEVITY &amp; <span class="tagline__alt">PRACTICALITY!</span>”</p>
    <div class="photo-band">
      <div class="photo photo--garden" role="img" aria-label="Photo of timber screening beside garden plants"></div>
      <div class="photo photo--pool" role="img" aria-label="Photo of a timber deck edging a blue swimming pool"></div>
      <div class="photo photo--boards" role="img" aria-label="Photo of close-up timber deck boards"></div>
      <div class="photo photo--spa" role="img" aria-label="Photo of a deck surrounding an outdoor spa"></div>
    </div>
    <div class="social">
      <span class="social__square"></span>
      <span class="social__text">Like us on Friendbook</span>
    </div>
  </section>
</body>
</html>
```